Business card design needed

i am a manufacturer of rocky road chocolate bars. my company is called tumbleberry confections p/l , trading as auntie mavis delights which we call our rocky road auntie mavis tumbleberry. we also retail lollies under the auntie mavis delights name from a shop front.our colours on the logo are burgandy and gold higlights.

Target Market(s)

retail and wholesale

Industry/Entity Type

Retail

Requirements
Must have
• company name and trading as name address phone numbers
tumbleberry confections
t/a auntie mavis delights
14 wattlebank st
brackenvale victoria 3187
tel 03 9481 5527
louise mobile 0417 389156
gordon mobile 0423 815 947
the designer can place the names and numbers where he/she thinks it would be appropriate.

```html
<!DOCTYPE html>
<html lang="en">
<head>
<meta charset="utf-8">
<title>Auntie Mavis Delights – Business Card</title>
<link rel="stylesheet" href="https://fonts.googleapis.com/css2?family=Cinzel:wght@400;700&family=Open+Sans:wght@400;600&display=swap">
<style>
  :root {
    --stage: #efe9df;
    --parchment-light: #ecd9ad;
    --parchment-mid: #dcc08a;
    --parchment-edge: #c9a56a;
    --burgundy: #7a1f55;
    --burgundy-dark: #4d1034;
    --ink: #3b2e1f;
    --white: #ffffff;
  }
  * { box-sizing: border-box; margin: 0; padding: 0; }
  html, body { width: 1200px; height: 800px; overflow: hidden; }
  body { background: var(--stage); position: relative; font-family: "Open Sans", sans-serif; }

  .card {
    position: absolute;
    width: 580px;
    height: 330px;
    overflow: hidden;
    background: radial-gradient(ellipse at 45% 40%, var(--parchment-light) 0%, var(--parchment-mid) 70%, var(--parchment-edge) 100%);
    box-shadow: 0 6px 18px rgba(0,0,0,0.18);
  }
  .card--back { left: 40px; top: 50px; }
  .card--front { left: 580px; top: 420px; }

  /* contact side */
  .name-tab {
    position: absolute; left: 0; top: 58px;
    width: 250px; height: 44px;
    background: var(--burgundy);
    border-radius: 0 22px 22px 0;
    color: var(--white);
    font-family: "Cinzel", serif; font-size: 23px; letter-spacing: 1px;
    display: flex; align-items: center; padding-left: 44px;
  }
  .role-tab {
    position: absolute; left: 0; top: 102px;
    width: 226px; height: 24px;
    background: var(--burgundy-dark);
    border-radius: 0 12px 12px 0;
    color: var(--white);
    font-family: "Cinzel", serif; font-size: 12px;
    display: flex; align-items: center; justify-content: flex-end; padding-right: 22px;
  }
  .brand-mark {
    position: absolute; right: 40px; top: 44px;
    width: 220px; text-align: center;
    display: flex; flex-direction: column; align-items: center; gap: 10px;
  }
  .brand-mark__dot { width: 18px; height: 18px; border-radius: 50%; background: var(--burgundy); }
  .brand-mark__name {
    font-family: "Cinzel", serif; font-weight: 700; font-size: 26px; line-height: 1.15;
    color: var(--burgundy);
  }
  .contact-list {
    position: absolute; left: 36px; bottom: 28px;
    list-style: none; color: var(--ink); font-size: 13px; line-height: 20px;
  }
  .contact-list li { display: flex; align-items: center; gap: 10px; }
  .contact-list .indent { padding-left: 22px; }
  .contact-list svg { width: 12px; height: 12px; flex: none; fill: var(--burgundy); }

  /* brand side */
  .card--front .brand-mark { left: 0; right: 0; margin: 0 auto; top: 70px; width: 300px; }
  .card--front .brand-mark__name { font-size: 36px; }
  .tagline-bar {
    position: absolute; left: 40px; right: 40px; bottom: 40px; height: 46px;
    background: var(--burgundy-dark);
    border-radius: 23px;
    color: var(--white); font-size: 19px; letter-spacing: 0.5px;
    display: flex; align-items: center; justify-content: center;
  }
</style>
</head>
<body>

<section class="card card--back" aria-label="Business card, contact side">
  <div class="name-tab">PETE HALLORIN</div>
  <div class="role-tab">Sales Executive</div>

  <div class="brand-mark">
    <span class="brand-mark__dot"></span>
    <span class="brand-mark__name">Auntie Mavis Tumbleberry</span>
  </div>

  <ul class="contact-list">
    <li><svg viewBox="0 0 12 12"><path d="M6 0a4 4 0 0 0-4 4c0 3 4 8 4 8s4-5 4-8a4 4 0 0 0-4-4zm0 5.5a1.5 1.5 0 1 1 0-3 1.5 1.5 0 0 1 0 3z"/></svg>14 wattlebank st brackenvale victoria 3187</li>
    <li><svg viewBox="0 0 12 12"><path d="M1 4c0-2 2-3 5-3s5 1 5 3v1H8V4H4v1H1zM2 6h8l1 5H1z"/></svg>+03 9481 5527</li>
    <li><svg viewBox="0 0 12 12"><rect x="3" y="0" width="6" height="12" rx="1"/></svg>0417 389156 ( louise )</li>
    <li class="indent">0423 815 947 ( gordon )</li>
    <li><svg viewBox="0 0 12 12"><path d="M0 2h12v8H0zM0 2l6 5 6-5" stroke="#ecd9ad" stroke-width="1"/></svg>petehallorin@tumbleberry.com</li>
    <li><svg viewBox="0 0 12 12"><circle cx="6" cy="6" r="5.5"/><path d="M0.5 6h11M6 0.5v11M3 2.5q3 3.5 0 7M9 2.5q-3 3.5 0 7" stroke="#ecd9ad" stroke-width="0.8" fill="none"/></svg>www.tumbleberry.com</li>
  </ul>
</section>

<section class="card card--front" aria-label="Business card, brand side">
  <div class="brand-mark">
    <span class="brand-mark__dot"></span>
    <span class="brand-mark__name">Auntie Mavis Tumbleberry</span>
  </div>
  <div class="tagline-bar">AUNTIE MAVIS DELIGHTS</div>
</section>

</body>
</html>
```